Web Design Corvane Mart is a market place for handcrafts products

design a landing home page , and a product page ,
for a market place CMS that will sell handcrafts ..

Target Market(s)

Market place for Handicrafts makers

Number of Pages Required

2 page

Requirements
Nice to have
• Search Google images for Marrakech Saffron Quarter , and Istanbul Copperleaf Arcade

```html
<!DOCTYPE html>
<html lang="en">
<head>
<meta charset="utf-8">
<title>Corvane Mart — Handmade Marketplace</title>
<link href="https://fonts.googleapis.com/css2?family=Jost:wght@300;400;500;600&display=swap" rel="stylesheet">
<style>
:root{
  --brand:#a3203a;
  --ink:#1e1e1e;
  --muted:#777;
  --line:#e6e6e6;
  --soft:#f3f3f3;
  --sand:#e7e2dc;
  --dark:#222;
  --darker:#1b1b1b;
  --badge:#f06a1d;
  --star:#f2b01e;
}
*{box-sizing:border-box;margin:0;padding:0}
html,body{width:1200px;height:3361px;overflow:hidden}
body{font-family:'Jost',sans-serif;color:var(--ink);background:#fff;font-size:12px}
a{color:inherit;text-decoration:none}
.wrap{width:730px;margin:0 auto;position:relative;height:100%}
section,header,footer,nav,div.bar{position:relative}

/* top bar */
.topbar{height:44px;background:var(--brand);color:#fff;font-size:8px}
.topbar .wrap{display:flex;align-items:center;justify-content:space-between}
.topbar .links{display:flex;gap:16px;align-items:center}
.topbar .links span{display:flex;align-items:center;gap:4px}
.topbar .sep{width:1px;height:12px;background:rgba(255,255,255,.5)}

/* header */
.header{height:66px;border-bottom:1px solid var(--line)}
.header .wrap{display:flex;align-items:center}
.logo{display:flex;flex-direction:column;align-items:center;width:102px}
.logo .dot{width:24px;height:24px;border-radius:50%;background:var(--badge)}
.logo .name{font-size:14px;letter-spacing:.5px;margin-top:3px}
.search{margin-left:86px;width:340px;border-bottom:1px solid var(--line);height:28px;display:flex;align-items:center;justify-content:space-between;padding:0 4px;color:var(--muted);font-size:9px}
.icons{margin-left:auto;display:flex;align-items:center;gap:14px}
.ico{position:relative}
.count{position:absolute;top:-6px;right:-6px;width:11px;height:11px;border-radius:50%;background:var(--brand);color:#fff;font-size:7px;display:flex;align-items:center;justify-content:center}
.cart-sum{font-size:7px;color:var(--muted);line-height:1.2}
.cart-sum b{display:block;font-size:12px;color:var(--ink);font-weight:600}

/* nav */
.mainnav{height:36px}
.mainnav .wrap{display:flex;align-items:center;font-size:9px}
.mainnav ul{display:flex;gap:22px;list-style:none}
.mainnav li.on{color:var(--brand)}
.mainnav .right{margin-left:auto;display:flex;gap:26px;align-items:center}
.mainnav .right span{display:flex;gap:5px;align-items:center}

/* hero */
.hero{height:485px}
.hero-photo{position:absolute;inset:0;background:linear-gradient(100deg,#f1f1f1 0%,#e4e3e0 35%,#d8d5cf 55%,#e2d5c0 75%,#c9a97e 100%)}
.hero-copy{position:absolute;left:235px;top:110px;width:440px}
.hero-copy .kicker{color:var(--brand);font-size:12px}
.hero-copy h1{font-size:39px;line-height:46px;font-weight:500;margin-top:10px;letter-spacing:.5px}
.hero-copy h1 span{font-weight:300}
.hero-copy p{font-size:9px;line-height:14px;color:#444;margin-top:30px;width:420px}
.btn-line{display:inline-flex;align-items:center;gap:6px;border:1px solid var(--ink);height:28px;padding:0 16px;font-size:8px;margin-top:26px}

/* promos */
.promos{height:279px;background:var(--soft)}
.promo-row{position:absolute;top:68px;left:0;right:0;display:flex;gap:27px}
.promo{width:225px;height:144px;background:var(--sand);padding:9px;flex:none}
.promo:nth-child(2){width:231px}
.promo:nth-child(3){width:231px}
.promo .frame{border:1px solid #9d9690;height:100%;position:relative;padding:12px}
.promo .pic{position:absolute;border-radius:4px}
.promo .tag{color:var(--brand);font-size:8px;text-transform:uppercase}
.promo h3{font-size:15px;font-weight:400;line-height:17px;margin:2px 0 6px}
.promo p{font-size:8px;line-height:11px;color:#444}

/* section heads */
.sec-head{text-align:center;padding-top:66px}
.sec-head small{font-size:9px;letter-spacing:.3px;text-transform:uppercase}
.sec-head h2{font-size:25px;font-weight:500;margin-top:6px}
.sec-head h2 em{font-style:normal;color:var(--brand)}
.sec-head .rule{width:92px;height:1px;background:var(--brand);margin:10px auto 0}

/* products */
.products{height:472px}
.prod-row{position:absolute;top:162px;left:0;right:0;display:flex;gap:19px}
.card{width:168px;height:243px;border:1px solid var(--line);background:#fff;position:relative;padding:0 12px;flex:none}
.card.active{box-shadow:0 4px 14px rgba(0,0,0,.12)}
.card .badge{position:absolute;left:9px;top:9px;width:24px;height:24px;border-radius:50%;background:var(--badge);color:#fff;font-size:6px;line-height:7px;text-align:center;padding-top:5px;z-index:2}
.card .img{height:125px;margin:10px 8px 0;border-radius:50%/40%}
.card .tools{position:absolute;right:10px;top:14px;display:flex;flex-direction:column;gap:6px}
.card .tools i{width:22px;height:22px;border-radius:50%;background:var(--darker);display:block}
.card hr{border:0;border-top:1px solid #d9b6bd;margin-top:6px}
.card .name{font-size:9px;font-weight:500;margin-top:9px}
.card .price{font-size:8px;margin-top:5px;color:var(--brand);font-weight:600}
.card .price s{color:#aaa;font-weight:400;margin-right:4px}
.card .price.plain{color:var(--ink)}
.stars{color:var(--star);font-size:10px;letter-spacing:1px;margin-top:2px}
.cart-btn{display:inline-flex;align-items:center;gap:6px;height:24px;padding:0 9px;border:1px solid #555;font-size:7px;margin-top:10px}
.card.active .cart-btn{background:var(--brand);border-color:var(--brand);color:#fff}
.arrow{position:absolute;top:272px;width:28px;height:28px;border-radius:50%;background:#eee;border:1px solid #ddd;display:flex;align-items:center;justify-content:center;color:#999;z-index:3}
.arrow.l{left:-15px}.arrow.r{right:-15px}
.dots{position:absolute;left:0;right:0;display:flex;justify-content:center;gap:5px}
.dots i{width:9px;height:9px;border-radius:50%;border:1px solid #ccc;display:block}
.dots i.on{background:var(--brand);border-color:var(--brand)}

/* collections */
.collections{height:480px;background:var(--soft)}
.offer{position:absolute;left:0;top:65px;width:355px;height:375px;background:linear-gradient(135deg,#ead6d0,#dfc0b8 60%,#e9d3cc)}
.offer-card{position:absolute;left:22px;top:90px;width:300px;height:195px;background:#fff;text-align:center;padding-top:48px}
.offer-card small{font-size:13px;font-weight:300;letter-spacing:.5px}
.offer-card h3{font-size:24px;font-weight:400;margin-top:8px}
.offer-card h3 em{font-style:normal;color:var(--brand)}
.btn-fill{display:inline-flex;align-items:center;gap:6px;background:var(--brand);color:#fff;font-size:8px;height:28px;padding:0 18px;margin-top:18px}
.coll-copy{position:absolute;left:374px;top:65px;width:356px}
.coll-copy small{font-size:9px}
.coll-copy h2{font-size:25px;font-weight:500;margin-top:6px}
.coll-copy h2 em{font-style:normal;color:var(--brand)}
.coll-copy p{font-size:8.5px;line-height:14px;color:#444;margin-top:14px}
.mini-row{position:absolute;left:374px;top:201px;display:flex;gap:19px}
.mini{width:106px;height:184px;background:#fff;border:1px solid var(--line);position:relative;padding:0 7px}
.mini .badge{position:absolute;left:7px;top:7px;width:20px;height:20px;border-radius:50%;background:var(--badge);color:#fff;font-size:5px;line-height:6px;text-align:center;padding-top:4px}
.mini .img{height:78px;margin:8px 10px 0;border-radius:50%}
.mini hr{border:0;border-top:1px solid #d9b6bd;margin-top:6px}
.mini .name{font-size:8px;font-weight:500;margin-top:6px}
.mini .price{font-size:7px;color:var(--brand);font-weight:600;margin-top:3px}
.mini .price s{color:#aaa;font-weight:400;margin-right:3px}
.mini .stars{font-size:8px}
.mini .cart-btn{height:20px;font-size:6px;padding:0 7px;margin-top:6px}

/* features */
.features{height:157px;background:var(--soft)}
.features .wrap{display:flex;align-items:center}
.feat{flex:1;text-align:center;border-right:1px solid var(--line);height:86px;padding-top:4px}
.feat:last-child{border:0}
.feat h4{font-size:12px;font-weight:500;margin-top:8px}
.feat p{font-size:9px;color:var(--muted);margin-top:3px}

/* blog */
.blog{height:436px}
.posts{position:absolute;top:152px;left:0;right:0;display:flex;gap:19px}
.post{width:231px}
.post .img{height:132px}
.post h4{font-size:11px;font-weight:500;margin-top:16px}
.post time{display:block;font-size:7px;color:#999;margin-top:10px}
.post p{font-size:8px;line-height:12px;color:#444;margin-top:8px}

/* subscribe */
.subscribe{height:187px;background:var(--dark);color:#fff;text-align:center;border-bottom:1px solid #3a3a3a}
.subscribe h2{font-size:24px;font-weight:400;padding-top:12px}
.subscribe p{font-size:9px;color:#ddd;margin-top:10px}
.sub-form{display:flex;justify-content:center;margin-top:12px}
.sub-form span{width:221px;height:28px;background:#fff;color:#888;font-size:9px;text-align:left;padding:8px 18px}
.sub-form b{width:87px;height:28px;background:var(--brand);font-size:8px;font-weight:500;display:flex;align-items:center;justify-content:center}

/* footer */
.footer{height:198px;background:var(--dark);color:#fff;text-align:center}
.foot-logo{padding-top:22px;display:flex;flex-direction:column;align-items:center}
.foot-logo i{width:46px;height:46px;border-radius:50%;background:var(--badge);display:block}
.foot-logo span{font-size:22px;letter-spacing:1px;margin-top:6px}
.foot-nav{display:flex;justify-content:center;gap:22px;font-size:9px;margin-top:18px;list-style:none}
.social{display:flex;justify-content:center;gap:8px;margin-top:16px}
.social i{width:20px;height:20px;background:var(--brand);display:block}
.copy{height:49px;background:var(--darker);color:#ccc;font-size:8px;display:flex;align-items:center;justify-content:center;gap:4px;border-top:1px solid #3a3a3a}
.copy em{font-style:normal;color:var(--brand)}
</style>
</head>
<body>

<div class="topbar bar">
  <div class="wrap">
    <span>Welcome to our international shop! Enjoy free shipping on orders $100 and up.</span>
    <div class="links">
      <span><svg width="11" height="8" viewBox="0 0 11 8" fill="none" stroke="#fff"><rect x=".5" y=".5" width="6" height="5"/><path d="M6.5 2.5h2.5l1.5 2v1h-4"/><circle cx="2.5" cy="6.5" r="1"/><circle cx="8.5" cy="6.5" r="1"/></svg>Order Tracker</span>
      <i class="sep"></i>
      <span><svg width="10" height="7" viewBox="0 0 10 7" fill="none" stroke="#fff"><rect x=".5" y=".5" width="9" height="6"/><path d="M.5.5 5 4 9.5.5"/></svg>Newsletter</span>
      <i class="sep"></i>
      <span>ENGLISH ⌄</span>
      <i class="sep"></i>
      <span>USD ⌄</span>
    </div>
  </div>
</div>

<header class="header">
  <div class="wrap">
    <a class="logo" href="#"><i class="dot"></i><span class="name">Corvane Mart</span></a>
    <div class="search"><span>Search</span>
      <svg width="14" height="14" viewBox="0 0 14 14" fill="none" stroke="#333" stroke-width="1.2"><circle cx="6" cy="6" r="5"/><path d="M9.5 9.5 13 13"/></svg>
    </div>
    <div class="icons">
      <svg width="14" height="15" viewBox="0 0 14 15" fill="none" stroke="#333" stroke-width="1.1"><circle cx="7" cy="4.5" r="3.5"/><path d="M1 14c0-3 2.7-5 6-5s6 2 6 5"/></svg>
      <span class="ico"><svg width="15" height="13" viewBox="0 0 15 13" fill="none" stroke="#333" stroke-width="1.1"><path d="M7.5 12S1 8 1 4a3 3 0 0 1 6.5-1A3 3 0 0 1 14 4c0 4-6.5 8-6.5 8z"/></svg><b class="count">0</b></span>
      <span class="ico"><svg width="16" height="14" viewBox="0 0 16 14" fill="none" stroke="#333" stroke-width="1.1"><path d="M1 4h14l-2 9H3z"/><path d="M5 4 8 1l3 3"/></svg><b class="count">0</b></span>
      <div class="cart-sum">My Shopping Cart<b>$299.49</b></div>
    </div>
  </div>
</header>

<nav class="mainnav">
  <div class="wrap">
    <ul><li class="on">Home</li><li>About</li><li>Shop ⌄</li><li>News</li><li>Faq</li><li>Contact</li></ul>
    <div class="right">
      <span><svg width="13" height="12" viewBox="0 0 13 12" fill="none" stroke="#333"><path d="M1.5 8V6a5 5 0 0 1 10 0v2"/><rect x="1" y="7" width="2.5" height="4"/><rect x="9.5" y="7" width="2.5" height="4"/></svg>(+01) 555 014 207</span>
      <span><svg width="10" height="13" viewBox="0 0 10 13" fill="none" stroke="#333"><path d="M5 12S1 7.5 1 5a4 4 0 0 1 8 0c0 2.5-4 7-4 7z"/><circle cx="5" cy="5" r="1.5"/></svg>Find Store</span>
    </div>
  </div>
</nav>

<section class="hero">
  <div class="hero-photo" role="img" aria-label="Speckled handmade ceramic cups and a tall sand-glazed vase on a pale table"></div>
  <div class="hero-copy">
    <div class="kicker">Sale up to 70% off</div>
    <h1>SHOPPING FOR<br><span>HANDMADE</span> PRODUCTS</h1>
    <p>Lorem ipsum dolor sit amet, consectetur adipiscing elit, sed do eiusmod tempor incididunt ut labore et dolore magna aliqua. Quis ipsum suspendisse ultrices gravida. Risus commodo viverra maecenas accumsan lacus vel facilisis.</p>
    <a class="btn-line" href="#">SHOP NOW! <svg width="12" height="7" viewBox="0 0 12 7" fill="none" stroke="#333"><path d="M0 3.5h11M8 .5l3 3-3 3"/></svg></a>
  </div>
</section>

<section class="promos">
  <div class="wrap">
    <div class="promo-row">
      <div class="promo"><div class="frame">
        <div class="pic" role="img" aria-label="Turquoise painted ceramic bowls" style="left:40px;top:6px;width:120px;height:40px;background:linear-gradient(90deg,#2aa7a0,#1a6f78)"></div>
        <div style="margin-top:40px"><div class="tag">Ocean Plate</div><h3>Ocean Plate Ceramic</h3><p>Lorem ipsum dolor sit amet, consectetur adipiscing elit. Mauris scelerisque convallis iaculis.</p></div>
      </div></div>
      <div class="promo"><div class="frame">
        <div class="pic" role="img" aria-label="Black and gold ornate vase" style="right:8px;top:8px;width:44px;height:108px;background:linear-gradient(180deg,#2b2520,#7a5a2a 55%,#2b2520)"></div>
        <div style="margin-top:18px;width:150px"><div class="tag">Pottery Vase</div><h3>Nib Vase Ripple Gold</h3><p>Lorem ipsum dolor sit amet, consectetur adipiscing elit. Mauris scelerisque convallis iaculis.</p></div>
      </div></div>
      <div class="promo"><div class="frame">
        <div class="pic" role="img" aria-label="Dark slim vase with dried flowers" style="left:12px;top:8px;width:30px;height:108px;background:linear-gradient(180deg,#c89a3a 0 25%,#e7e2dc 25% 40%,#3b342f 40%)"></div>
        <div style="margin-left:54px;margin-top:4px"><div class="tag">Handmade Vase</div><h3>Octogonal Gilded Pottery Gold</h3><p>Lorem ipsum dolor sit amet, consectetur adipiscing elit. Mauris scelerisque convallis iaculis.</p></div>
      </div></div>
    </div>
  </div>
</section>

<section class="products">
  <div class="wrap">
    <div class="sec-head"><small>Hot Deal</small><h2>Trending This <em>Week</em></h2><div class="rule"></div></div>
    <span class="arrow l">‹</span><span class="arrow r">›</span>
    <div class="prod-row">
      <article class="card"><span class="badge">-30%<br>OFF</span><div class="img" role="img" aria-label="Floral painted ceramic jug" style="background:linear-gradient(135deg,#e9e3ff,#d7663a 40%,#3d5aa8 70%,#f2d04a)"></div><hr><div class="name">Vase Flower Minimal</div><div class="price"><s>$55.00</s>$35.00</div><div class="stars">★★★★★</div><a class="cart-btn" href="#">ADD TO CART <svg width="8" height="9" viewBox="0 0 8 9" fill="none" stroke="currentColor"><path d="M.5 3h7v5.5h-7zM2.5 3V2a1.5 1.5 0 0 1 3 0v1"/></svg></a></article>
      <article class="card active"><span class="badge">-30%<br>OFF</span><div class="tools"><i></i><i></i><i></i></div><div class="img" role="img" aria-label="Chinese ceramic bowl with red painted spoon" style="background:linear-gradient(160deg,#f5f5f5,#e2e2e2 50%,#c23a3a 60%,#efefef);margin-right:34px"></div><hr><div class="name">Chinese Cutlery</div><div class="price plain">$50.00</div><div class="stars">★★★★★</div><a class="cart-btn" href="#">ADD TO CART <svg width="8" height="9" viewBox="0 0 8 9" fill="none" stroke="currentColor"><path d="M.5 3h7v5.5h-7zM2.5 3V2a1.5 1.5 0 0 1 3 0v1"/></svg></a></article>
      <article class="card"><span class="badge">-30%<br>OFF</span><div class="img" role="img" aria-label="Plum glazed tagine dish" style="background:linear-gradient(180deg,#5b2c43,#3b1a2a)"></div><hr><div class="name">Mini Moroccan Ceramic</div><div class="price"><s>$40.00</s>$25.00</div><div class="stars">★★★★★</div><a class="cart-btn" href="#">ADD TO CART <svg width="8" height="9" viewBox="0 0 8 9" fill="none" stroke="currentColor"><path d="M.5 3h7v5.5h-7zM2.5 3V2a1.5 1.5 0 0 1 3 0v1"/></svg></a></article>
      <article class="card"><span class="badge">-30%<br>OFF</span><div class="img" role="img" aria-label="Terracotta sake jar" style="background:linear-gradient(180deg,#8a3c22,#c25a35)"></div><hr><div class="name">Sake Jar Ripple</div><div class="price"><s>$69.00</s>$49.00</div><div class="stars">★★★★★</div><a class="cart-btn" href="#">ADD TO CART <svg width="8" height="9" viewBox="0 0 8 9" fill="none" stroke="currentColor"><path d="M.5 3h7v5.5h-7zM2.5 3V2a1.5 1.5 0 0 1 3 0v1"/></svg></a></article>
    </div>
    <div class="dots" style="top:425px"><i></i><i class="on"></i><i></i></div>
  </div>
</section>

<section class="collections">
  <div class="wrap">
    <div class="offer" role="img" aria-label="Blush pink gift wrapping with ribbon and a pearl ornament">
      <div class="offer-card">
        <small>SPECIAL OFFER</small>
        <h3>50% Off <em>Gift Sets</em></h3>
        <a class="btn-fill" href="#">SHOP NOW! <svg width="12" height="7" viewBox="0 0 12 7" fill="none" stroke="#fff"><path d="M0 3.5h11M8 .5l3 3-3 3"/></svg></a>
      </div>
    </div>
    <div class="coll-copy">
      <small>OUR COLLECTIONS</small>
      <h2><em>New</em> Collections</h2>
      <p>Lorem ipsum dolor sit amet, consectetur adipiscing elit. Mauris scelerisque convallis iaculis. Morbi convallis vel urna sed cursus. Nullam magna nibh, ornare eget ex quis, efficitur luctus orci. Nulla mi urna, aliquet id mattis non, feugiat vel nisi.</p>
    </div>
    <span class="arrow l" style="left:359px;top:253px;width:24px;height:24px">‹</span>
    <span class="arrow r" style="right:-12px;top:253px;width:24px;height:24px">›</span>
    <div class="mini-row">
      <article class="mini"><span class="badge">-30%<br>OFF</span><div class="img" role="img" aria-label="Red and black ceramic bowl" style="background:linear-gradient(180deg,#111 40%,#d63a2a 40%)"></div><hr><div class="name">Chinese Ceramic Bowl</div><div class="price"><s>$69.00</s>$49.00</div><div class="stars">★★★★★</div><a class="cart-btn" href="#">ADD TO CART ⌂</a></article>
      <article class="mini"><span class="badge">-30%<br>OFF</span><div class="img" role="img" aria-label="Pale blue abstract divided plate" style="background:radial-gradient(#e9efee,#9fb5b4)"></div><hr><div class="name">Plate Divided Abstract</div><div class="price"><s>$69.00</s>$49.00</div><div class="stars">★★★★★</div><a class="cart-btn" href="#">ADD TO CART ⌂</a></article>
      <article class="mini"><span class="badge">-30%<br>OFF</span><div class="img" role="img" aria-label="Painted porcelain jewelry box" style="background:linear-gradient(135deg,#f2efe8,#c9b57a 50%,#5c6fa8)"></div><hr><div class="name">Mini Box Jewelry</div><div class="price"><s>$69.00</s>$49.00</div><div class="stars">★★★★★</div><a class="cart-btn" href="#">ADD TO CART ⌂</a></article>
    </div>
    <div class="dots" style="top:398px;left:374px;right:0"><i></i><i class="on"></i><i></i></div>
  </div>
</section>

<section class="products">
  <div class="wrap">
    <div class="sec-head"><small>Best Sellers</small><h2>Our <em>Best</em> Sellers</h2></div>
    <span class="arrow l">‹</span><span class="arrow r">›</span>
    <div class="prod-row">
      <article class="card"><span class="badge">-30%<br>OFF</span><div class="img" role="img" aria-label="Floral painted ceramic jug" style="background:linear-gradient(135deg,#e9e3ff,#d7663a 40%,#3d5aa8 70%,#f2d04a)"></div><hr><div class="name">Vase Flower Minimal</div><div class="price"><s>$55.00</s>$35.00</div><div class="stars">★★★★★</div><a class="cart-btn" href="#">ADD TO CART <svg width="8" height="9" viewBox="0 0 8 9" fill="none" stroke="currentColor"><path d="M.5 3h7v5.5h-7zM2.5 3V2a1.5 1.5 0 0 1 3 0v1"/></svg></a></article>
      <article class="card active"><span class="badge">-30%<br>OFF</span><div class="tools"><i></i><i></i><i></i></div><div class="img" role="img" aria-label="Chinese ceramic bowl with red painted spoon" style="background:linear-gradient(160deg,#f5f5f5,#e2e2e2 50%,#c23a3a 60%,#efefef);margin-right:34px"></div><hr><div class="name">Chinese Cutlery</div><div class="price plain">$50.00</div><div class="stars">★★★★★</div><a class="cart-btn" href="#">ADD TO CART <svg width="8" height="9" viewBox="0 0 8 9" fill="none" stroke="currentColor"><path d="M.5 3h7v5.5h-7zM2.5 3V2a1.5 1.5 0 0 1 3 0v1"/></svg></a></article>
      <article class="card"><span class="badge">-30%<br>OFF</span><div class="img" role="img" aria-label="Plum glazed tagine dish" style="background:linear-gradient(180deg,#5b2c43,#3b1a2a)"></div><hr><div class="name">Mini Moroccan Ceramic</div><div class="price"><s>$40.00</s>$25.00</div><div class="stars">★★★★★</div><a class="cart-btn" href="#">ADD TO CART <svg width="8" height="9" viewBox="0 0 8 9" fill="none" stroke="currentColor"><path d="M.5 3h7v5.5h-7zM2.5 3V2a1.5 1.5 0 0 1 3 0v1"/></svg></a></article>
      <article class="card"><span class="badge">-30%<br>OFF</span><div class="img" role="img" aria-label="Terracotta sake jar" style="background:linear-gradient(180deg,#8a3c22,#c25a35)"></div><hr><div class="name">Sake Jar Ripple</div><div class="price"><s>$69.00</s>$49.00</div><div class="stars">★★★★★</div><a class="cart-btn" href="#">ADD TO CART <svg width="8" height="9" viewBox="0 0 8 9" fill="none" stroke="currentColor"><path d="M.5 3h7v5.5h-7zM2.5 3V2a1.5 1.5 0 0 1 3 0v1"/></svg></a></article>
    </div>
    <div class="dots" style="top:425px"><i></i><i class="on"></i><i></i></div>
  </div>
</section>

<section class="features">
  <div class="wrap">
    <div class="feat"><svg width="28" height="26" viewBox="0 0 28 26" fill="none" stroke="#555"><rect x="2" y="6" width="18" height="16"/><path d="M2 6l4-5h10l4 5M11 1v21"/><circle cx="22" cy="19" r="5" fill="#fff"/></svg><h4>Free Easy Returns</h4><p>Return to 7 days</p></div>
    <div class="feat"><svg width="30" height="26" viewBox="0 0 30 26" fill="none" stroke="#555"><rect x="2" y="4" width="17" height="14"/><path d="M19 9h6l3 4v5h-9"/><circle cx="7" cy="20" r="2.5"/><circle cx="23" cy="20" r="2.5"/><path d="M7 14l6-7"/></svg><h4>Free Delivery Monday</h4><p>Orders over $149</p></div>
    <div class="feat"><svg width="28" height="26" viewBox="0 0 28 26" fill="none" stroke="#555"><path d="M4 3l5 1 2 5-3 2a12 12 0 0 0 6 6l2-3 5 2 1 5c-10 2-20-8-18-18z"/><rect x="16" y="1" width="10" height="7" rx="2"/></svg><h4>All Day Support</h4><p>24/7 Support care</p></div>
    <div class="feat"><svg width="26" height="28" viewBox="0 0 26 28" fill="none" stroke="#555"><path d="M13 2l10 4v7c0 7-5 11-10 13C8 24 3 20 3 13V6z"/><path d="M8 14l4 4 6-7"/></svg><h4>Secure Checkout</h4><p>100% protected by Veripay</p></div>
  </div>
</section>

<section class="blog">
  <div class="wrap">
    <div class="sec-head"><small>Blog</small><h2>Latest From Our <em>Blog</em></h2></div>
    <div class="posts">
      <article class="post"><div class="img" role="img" aria-label="Stacks of glazed pottery bowls at a market stall" style="background:linear-gradient(135deg,#3b3a2c,#b6a48a 45%,#5d7a6a 70%,#2c2a22)"></div><h4>The Making Of A California Classic</h4><time>October 08, 2021</time><p>Lorem ipsum dolor sit amet, consectetur adipiscing elit. Mauris scelerisque convallis iaculis.</p></article>
      <article class="post"><div class="img" role="img" aria-label="Ceramic vases beside a framed print" style="background:linear-gradient(90deg,#3a3a3a,#8f8a80 40%,#d8d0b8 70%,#4b4b4b)"></div><h4>This Years Most Beloved Pieces</h4><time>September 20, 2021</time><p>Lorem ipsum dolor sit amet, consectetur adipiscing elit. Mauris scelerisque convallis iaculis.</p></article>
      <article class="post"><div class="img" role="img" aria-label="White ceramic teapot on a grey workbench" style="background:linear-gradient(135deg,#4a4a48,#a9a7a2 50%,#e3e1dc 65%,#5a5955)"></div><h4>Choosing A Glaze With Kramic</h4><time>October 20, 2021</time><p>Lorem ipsum dolor sit amet, consectetur adipiscing elit. Mauris scelerisque convallis iaculis.</p></article>
    </div>
  </div>
</section>

<section class="subscribe">
  <svg style="margin-top:30px" width="22" height="20" viewBox="0 0 22 20" fill="none" stroke="#a3203a" stroke-width="1.2"><path d="M1 8l10-7 10 7v11H1z"/><path d="M1 8l10 6 10-6"/></svg>
  <h2>Subscribe</h2>
  <p>Get on the list and get 10% off your first order!</p>
  <div class="sub-form"><span>Enter Your E-Mail Address</span><b>SUBSCRIBE</b></div>
</section>

<footer class="footer">
  <div class="foot-logo"><i></i><span>CORVANE MART</span></div>
  <ul class="foot-nav"><li>Home</li><li>About</li><li>Shop</li><li>News</li><li>Faq</li><li>Contact</li></ul>
  <div class="social"><i></i><i></i><i></i><i></i></div>
</footer>
<div class="copy bar">Copyright © 2021 Corvane Mart. All Rights Reserved | <em>(+01) 555 014 207</em> | hello@corvanemart.test</div>

</body>
</html>
```